I have a new startup... www.hirebybrindle.com
An issue Im running into is when people create profiles there banner images are getting messed up. So instead I would like anywhere to 10-15 banners created as stock banners for my site the people signing up need to choose from so the website looks more in uniform. The site contains graphic designers, photographers, & videographers so maybe some banners can be patterns of a camera outline or graphic design tools etc. Need really clean and sleek looking banners that these people can pick from that will make sense.
I will attach my logo if you want to do a cool "Brindle" pattern design as a banner.
Banner sizes 2000px by 560px.

If you have any questions please let me know.

```html
<!DOCTYPE html>
<html lang="en">
<head>
<meta charset="utf-8">
<title>Hire by Brindle – Stock Profile Banners</title>
<link href="https://fonts.googleapis.com/css2?family=Roboto+Condensed:wght@300;400;700&display=swap" rel="stylesheet">
<style>
  :root {
    --page-bg: #000000;
    --banner-border: #5a5a5a;
    --rust: #b33a1a;
    --ink: #050505;
    --title: #f4f4f4;
    --subtitle: #d6d6d6;
    --url: #ffffff;
    --glow: rgba(230, 80, 30, 0.38);
  }
  * { margin: 0; padding: 0; box-sizing: border-box; }
  html, body {
    width: 1200px; height: 1091px; overflow: hidden;
    background: var(--page-bg);
    font-family: "Roboto Condensed", "Arial Narrow", sans-serif;
  }
  .sheet { position: relative; width: 1200px; height: 1091px; }

  .banner {
    position: absolute; left: 119px; width: 965px; height: 274px;
    border: 2px solid var(--banner-border);
    background: var(--ink);
    overflow: hidden;
  }
  .banner--photographers { top: 114px; }
  .banner--videographers { top: 416px; }
  .banner--designers { top: 735px; }

  .banner__shape { position: absolute; inset: 0; width: 100%; height: 100%; }

  .banner__photo { position: absolute; top: 0; right: 0; height: 100%; }
  .banner--photographers .banner__photo {
    width: 440px;
    background: linear-gradient(90deg, rgba(0,0,0,0) 0%, rgba(60,48,42,0.55) 40%, rgba(90,78,70,0.75) 75%, rgba(70,60,55,0.8) 100%);
  }
  .banner--videographers .banner__photo {
    width: 470px;
    background: linear-gradient(90deg, rgba(0,0,0,0) 0%, rgba(50,52,66,0.6) 40%, rgba(92,94,110,0.8) 80%, rgba(120,122,136,0.85) 100%);
  }
  .banner--designers .banner__photo {
    width: 520px;
    background: linear-gradient(90deg, rgba(0,0,0,0) 0%, rgba(70,60,50,0.55) 35%, rgba(110,100,92,0.75) 70%, rgba(80,110,90,0.7) 100%);
  }

  .banner__streaks {
    position: absolute; left: 230px; top: 0; width: 420px; height: 100%;
    background: radial-gradient(ellipse 60% 55% at 45% 70%, var(--glow) 0%, rgba(200,60,20,0.12) 55%, rgba(0,0,0,0) 80%);
  }

  .banner__art { position: absolute; }
  .banner--photographers .banner__art {
    left: 93px; top: 65px; width: 143px; height: 208px;
    background: linear-gradient(180deg, #2a2a2a 0%, #121212 55%, #3a3a3a 100%);
    border-radius: 8px 8px 0 0;
  }
  .banner--videographers .banner__art {
    left: 61px; top: 63px; width: 163px; height: 210px;
    background: linear-gradient(180deg, #cfcfcf 0%, #8d8d8d 25%, #1e1e1e 45%, #141414 100%);
    border-radius: 30px 30px 0 0;
  }
  .banner--designers .banner__art {
    left: 46px; top: 45px; width: 253px; height: 220px;
    background: linear-gradient(135deg, #4a4a4a 0%, #e0803a 40%, #3c8a55 60%, #e9e4d8 100%);
    border-radius: 12px;
    opacity: 0.9;
  }

  .banner__label {
    position: absolute; white-space: nowrap; line-height: 1;
    text-transform: uppercase;
  }
  .label--minor {
    font-weight: 300; font-size: 23px; letter-spacing: 8.5px;
    color: var(--subtitle);
  }
  .label--minor.label--tight { letter-spacing: 5px; }
  .label--major {
    font-weight: 400; font-size: 56px; letter-spacing: 0.5px;
    color: var(--title);
  }
  .banner__url {
    position: absolute; white-space: nowrap; line-height: 1;
    font-weight: 700; font-size: 23px; letter-spacing: 2.6px;
    color: var(--url);
  }
  .banner__cursor { position: absolute; width: 32px; height: 36px; }
</style>
</head>
<body>
<main class="sheet">

  <!-- Photographers banner -->
  <section class="banner banner--photographers">
    <svg class="banner__shape" viewBox="0 0 961 270" preserveAspectRatio="none" aria-hidden="true">
      <rect width="961" height="270" fill="var(--rust)"/>
      <polygon points="362,0 961,0 961,270 432,270 228,138" fill="var(--ink)"/>
    </svg>
    <div class="banner__streaks" role="img" aria-label="Glowing orange light streaks"></div>
    <div class="banner__photo" role="img" aria-label="Photo of a photographer holding a camera up to shoot"></div>
    <div class="banner__art" role="img" aria-label="Illustration of a DSLR camera on a tripod"></div>
    <span class="banner__label label--minor" style="left:333px; top:62px;">Videographers</span>
    <span class="banner__label label--major" style="left:277px; top:95px;">Photographers</span>
    <span class="banner__label label--minor label--tight" style="left:441px; top:155px;">Graphic Designer</span>
    <span class="banner__url" style="left:625px; top:210px;">www.hirebybrindle.com</span>
  </section>

  <!-- Videographers banner -->
  <section class="banner banner--videographers">
    <svg class="banner__shape" viewBox="0 0 961 270" preserveAspectRatio="none" aria-hidden="true">
      <rect width="961" height="270" fill="var(--rust)"/>
      <polygon points="360,0 961,0 961,270 432,270 222,138" fill="var(--ink)"/>
    </svg>
    <div class="banner__streaks" role="img" aria-label="Glowing orange light streaks"></div>
    <div class="banner__photo" role="img" aria-label="Photo of a videographer operating a professional video camera"></div>
    <div class="banner__art" role="img" aria-label="Illustration of a vintage film projector on a tripod"></div>
    <span class="banner__label label--minor" style="left:342px; top:79px;">Photographers</span>
    <span class="banner__label label--major" style="left:286px; top:111px;">Videographers</span>
    <span class="banner__label label--minor label--tight" style="left:449px; top:169px;">Graphic Designer</span>
    <span class="banner__url" style="left:604px; top:218px;">www.hirebybrindle.com</span>
    <svg class="banner__cursor" style="left:906px; top:220px;" viewBox="0 0 32 36" aria-hidden="true">
      <polygon points="2,1 2,30 9,23 15,35 20,33 14,21 24,21" fill="#ffffff"/>
    </svg>
  </section>

  <!-- Graphic designer banner -->
  <section class="banner banner--designers">
    <svg class="banner__shape" viewBox="0 0 961 270" preserveAspectRatio="none" aria-hidden="true">
      <rect width="961" height="270" fill="var(--rust)"/>
      <polygon points="360,0 961,0 961,270 432,270 240,138" fill="var(--ink)"/>
    </svg>
    <div class="banner__streaks" role="img" aria-label="Glowing orange light streaks"></div>
    <div class="banner__photo" role="img" aria-label="Photo of a designer's desk with laptop, camera and colour swatches"></div>
    <div class="banner__art" role="img" aria-label="Illustration of a drawing tablet with stylus, pencils, notebooks and a coffee cup"></div>
    <span class="banner__label label--minor" style="left:366px; top:75px;">Photographers</span>
    <span class="banner__label label--major" style="left:318px; top:108px;">Graphic Designer</span>
    <span class="banner__label label--minor" style="left:434px; top:173px;">Videographers</span>
    <span class="banner__url" style="left:606px; top:222px;">www.hirebybrindle.com</span>
    <svg class="banner__cursor" style="left:911px; top:224px;" viewBox="0 0 32 36" aria-hidden="true">
      <polygon points="2,1 2,30 9,23 15,35 20,33 14,21 24,21" fill="#ffffff"/>
    </svg>
  </section>

</main>
</body>
</html>
```